kestrova business cards

Hey design gurus!
I'm after a clean, modern, stylish business card for my about to be launched company.
I've uploaded the logos for my company "Kestrova Electrical Solutions"
and also the tarrow alliance logo to whom i am associated.

```html
<!DOCTYPE html>
<html lang="en">
<head>
<meta charset="utf-8">
<title>Kestrova Electrical Solutions – Business Cards</title>
<link href="https://fonts.googleapis.com/css2?family=Michroma&family=Arimo:wght@400&display=swap" rel="stylesheet">
<style>
  :root {
    --stage: #3a3a3c;
    --card: #0c1824;
    --card-deep: #050c14;
    --blue: #1a8fe0;
    --blue-soft: #1d5b86;
    --white: #ffffff;
    --badge-line: #b5504a;
  }
  * { box-sizing: border-box; margin: 0; padding: 0; }
  html, body { width: 1200px; height: 901px; overflow: hidden; }
  body {
    background: var(--stage);
    font-family: "Arimo", Arial, sans-serif;
    color: var(--white);
    position: relative;
  }
  .card {
    position: absolute;
    left: 290px;
    width: 620px;
    height: 354px;
    background: linear-gradient(135deg, var(--card) 0%, var(--card-deep) 100%);
    border-left: 4px solid var(--blue);
    border-bottom: 4px solid var(--blue);
    overflow: hidden;
    box-shadow: 0 10px 24px rgba(0,0,0,.45);
  }
  .card--back { top: 66px; }
  .card--front { top: 470px; }

  .brand { display: flex; align-items: center; gap: 12px; position: absolute; }
  .brand__dot {
    width: 50px; height: 50px; border-radius: 50%;
    background: var(--blue);
  }
  .brand__name {
    font-family: "Michroma", sans-serif;
    color: var(--blue);
    font-size: 27px;
    line-height: 1;
    letter-spacing: 1px;
  }
  .brand__tag {
    font-family: "Michroma", sans-serif;
    color: var(--white);
    font-size: 9.5px;
    letter-spacing: 2.6px;
    margin-top: 5px;
  }

  /* back */
  .back__pattern {
    position: absolute; inset: 0;
    background: radial-gradient(ellipse at 80% 70%, rgba(29,91,134,.55), transparent 60%),
                linear-gradient(135deg, #18252f 0%, #0a141d 55%, #0f2233 100%);
  }
  .card--back .brand { left: 175px; top: 118px; }
  .badge {
    position: absolute; left: 250px; top: 212px;
    width: 160px; height: 54px;
    border: 1.5px solid var(--badge-line);
    border-radius: 5px;
    background: rgba(5,12,20,.85);
    display: flex; align-items: center; padding-left: 12px;
  }
  .badge__mark { width: 36px; height: 36px; background: var(--white); border-radius: 3px; }

  /* front */
  .card--front .brand { left: 22px; top: 26px; }
  .front__mark {
    position: absolute; right: 20px; bottom: 14px;
    width: 280px; height: 240px;
    border-radius: 50% 50% 12px 50%;
    background: radial-gradient(circle at 55% 45%, rgba(29,91,134,.7), rgba(12,24,36,0) 70%);
  }
  .holder {
    position: absolute; right: 36px; top: 98px; text-align: right;
  }
  .holder__name {
    font-family: "Michroma", sans-serif;
    color: var(--blue);
    font-size: 17px; letter-spacing: 1.5px;
  }
  .holder__role { font-size: 16px; margin-top: 4px; }
  .holder__bar {
    position: absolute; right: 10px; top: 106px;
    width: 9px; height: 42px; background: var(--blue);
  }
  .address { position: absolute; left: 44px; top: 178px; font-size: 16.5px; line-height: 1.3; }
  .contact { position: absolute; left: 34px; top: 244px; list-style: none; font-size: 17.5px; }
  .contact li { display: flex; align-items: center; gap: 10px; height: 30px; }
  .contact svg { width: 17px; height: 17px; fill: none; stroke: var(--blue); stroke-width: 1.6; }
</style>
</head>
<body>

<section class="card card--back" aria-label="Card back">
  <div class="back__pattern" role="img" aria-label="Repeating brand monogram pattern in embossed navy and blue"></div>
  <div class="brand">
    <span class="brand__dot"></span>
    <div>
      <div class="brand__name">KESTROVA</div>
      <div class="brand__tag">ELECTRICAL SOLUTIONS</div>
    </div>
  </div>
  <div class="badge" role="img" aria-label="Tarrow Alliance member badge">
    <span class="badge__mark"></span>
  </div>
</section>

<section class="card card--front" aria-label="Card front">
  <div class="front__mark" role="img" aria-label="Large embossed brand monogram with plug cable"></div>
  <div class="brand">
    <span class="brand__dot"></span>
    <div>
      <div class="brand__name">KESTROVA</div>
      <div class="brand__tag">ELECTRICAL SOLUTIONS</div>
    </div>
  </div>
  <div class="holder">
    <div class="holder__name">DORIAN VALE</div>
    <div class="holder__role">Manager</div>
  </div>
  <span class="holder__bar"></span>
  <address class="address" style="font-style:normal">Your Address, City<br>State, Zip 0000</address>
  <ul class="contact">
    <li><svg viewBox="0 0 20 20"><path d="M4 2l3 1 1 4-2 1a10 10 0 0 0 6 6l1-2 4 1 1 3-2 2C9 18 2 11 2 4z"/></svg>123-456-2100</li>
    <li><svg viewBox="0 0 20 20"><rect x="2" y="4" width="16" height="12"/><path d="M2 4l8 7 8-7"/></svg>youremail@mailbox.com</li>
    <li><svg viewBox="0 0 20 20"><circle cx="10" cy="10" r="8"/><path d="M2 10h16M10 2c3 3 3 13 0 16M10 2c-3 3-3 13 0 16"/></svg>www.yourwebsite.com</li>
  </ul>
</section>

</body>
</html>
```